Stonebay Towing Business Card

Towing
Accident towing
Mechanical breakdown
Insurance, salvage and recovery
4wd off road towing
Light & Heavy towing
8347 2516
24 hour business 7 days

Logo can be whole size on front

Industry/Entity Type

Towing/ transport

Contact Information for Business Card

The above

```html
<!DOCTYPE html>
<html lang="en">
<head>
<meta charset="utf-8">
<title>Stonebay Towing Business Card</title>
<link rel="stylesheet" href="https://fonts.googleapis.com/css2?family=Roboto:wght@400;500;700&display=swap">
<style>
  :root {
    --backdrop: #777777;
    --card-white: #ffffff;
    --brand-red: #d42027;
    --text-light: #ffffff;
  }
  * { box-sizing: border-box; margin: 0; padding: 0; }
  html, body {
    width: 1200px;
    height: 1200px;
    overflow: hidden;
    background: var(--backdrop);
    font-family: "Roboto", Arial, sans-serif;
  }
  .card {
    position: absolute;
    left: 165px;
    width: 869px;
    height: 508px;
    background: var(--card-white);
    overflow: hidden;
  }
  .card--front { top: 76px; }
  .card--back { top: 626px; }

  .front-panel {
    position: absolute;
    inset: 0;
    width: 100%;
    height: 100%;
  }
  .front-panel polygon { fill: var(--brand-red); }

  .services {
    position: absolute;
    left: 74px;
    top: 228px;
    list-style: none;
    color: var(--text-light);
    font-size: 22px;
    font-weight: 400;
    line-height: 33px;
  }
  .services li::before {
    content: "•";
    margin-right: 6px;
  }

  .phone {
    position: absolute;
    left: 527px;
    top: 339px;
    height: 87px;
    display: flex;
    align-items: center;
    gap: 14px;
    color: var(--text-light);
    font-size: 41px;
    font-weight: 500;
    letter-spacing: 0.5px;
  }
  .phone svg { width: 30px; height: 30px; fill: var(--text-light); }

  .brand-name {
    position: absolute;
    color: var(--brand-red);
    font-weight: 700;
    white-space: nowrap;
    transform: translate(-50%, -50%);
  }
  .brand-name--front { left: 648px; top: 150px; font-size: 40px; }
  .brand-name--back { left: 435px; top: 250px; font-size: 76px; }
</style>
</head>
<body>
  <section class="card card--front">
    <svg class="front-panel" viewBox="0 0 869 508" preserveAspectRatio="none" aria-hidden="true">
      <polygon points="0,0 501,339 869,339 869,426 501,426 423,508 0,508"/>
    </svg>
    <ul class="services">
      <li>Towing</li>
      <li>Accident towing</li>
      <li>Mechanical breakdown</li>
      <li>Insurance, salvage and recovery</li>
      <li>4wd off road towing</li>
      <li>Light &amp; Heavy towing</li>
    </ul>
    <div class="phone">
      <span class="phone-number">8347 2516</span>
      <svg viewBox="0 0 24 24" aria-hidden="true">
        <path d="M6.6 10.8c1.4 2.8 3.8 5.1 6.6 6.6l2.2-2.2c.3-.3.7-.4 1-.2 1.1.4 2.3.6 3.6.6.6 0 1 .4 1 1V20c0 .6-.4 1-1 1C10.6 21 3 13.4 3 4c0-.6.4-1 1-1h3.5c.6 0 1 .4 1 1 0 1.3.2 2.5.6 3.6.1.3 0 .7-.2 1L6.6 10.8z"/>
      </svg>
    </div>
    <div class="brand-name brand-name--front">Stonebay Towing</div>
  </section>

  <section class="card card--back">
    <div class="brand-name brand-name--back">Stonebay Towing</div>
  </section>
</body>
</html>
```